Gluten Free Bakery Relaunch Ad series

Would like a series of three cohesive ads for use in social media to build buzz leading up to our grand reopening May 1st. Would like to use a single existing product photo as the PRIMARY background in each ad, featuring text along the lines of "gluten free never looked so good," "the wait is over," or something similar as well as the company name "CRUMB: A Harbor Bakery." Feel free to visit www.crumbovenhouse.com, facebook.com/CrumbOvenHouse or @CrumbOvenHouse for more info on the background/feel of the company. Thanks!

Target Market(s)

Gluten free diet, age 20-40, for use on social media

Industry/Entity Type

It Company

Font styles to use
Serif
Sans Serif

Colors
ffffff

Requirements
Must have
• Include reopening date "May 1st", not too feminine
Nice to have
• You are not wedded to the example slogans above. Please feel free to experiment with creative or catchy tag lines.

Big fan of the following fonts, just as an example, not mandatory: Pluto, Gotham, Oxtail

```html
<!DOCTYPE html>
<html lang="en">
<head>
<meta charset="utf-8">
<title>CRUMB Reopening Ad Series</title>
<link href="https://fonts.googleapis.com/css2?family=Ultra&family=Oswald:wght@500&display=swap" rel="stylesheet">
<style>
  :root {
    --stage: #e6e6e6;
    --cream: #f6f3e8;
    --red: #ad2427;
    --ink: #1f1a17;
    --white: #ffffff;
  }
  html, body { margin: 0; padding: 0; overflow: hidden; }
  body { width: 1200px; height: 1000px; background: var(--stage); position: relative; }
  .ad {
    position: absolute; width: 505px; height: 505px; background: var(--cream);
    overflow: hidden; box-shadow: 0 1px 3px rgba(0,0,0,0.12);
  }
  .ad--chip { left: 71px; top: 42px; }
  .ad--gluten { left: 611px; top: 40px; width: 507px; height: 507px; }
  .ad--oat { left: 352px; top: 436px; z-index: 2; }
  .photo { position: absolute; left: 0; top: 0; width: 100%; height: 318px; }
  .photo--chip { background: radial-gradient(ellipse at 60% 70%, #d8b88a 0%, #b78d5c 45%, #7a5533 80%, #5b5f74 100%); }
  .photo--gluten { background: radial-gradient(ellipse at 55% 50%, #8a5d45 0%, #5b3727 45%, #2a1712 80%, #120b09 100%); }
  .photo--oat { background: radial-gradient(ellipse at 50% 55%, #d9a865 0%, #b47a3d 40%, #6e4522 75%, #1a120d 100%); }
  .torn { position: absolute; left: 0; top: 308px; width: 100%; height: 14px; }
  .headline {
    position: absolute; left: 0; right: 0; top: 0; text-align: center; color: var(--white);
    font-family: "Ultra", Georgia, serif; text-shadow: 0 2px 8px rgba(0,0,0,0.35);
  }
  .headline span { display: block; position: absolute; left: 0; right: 0; line-height: 1; }
  .headline em { font-style: italic; }
  .ribbon { position: absolute; right: 0; top: 0; width: 125px; height: 125px; }
  .logo {
    position: absolute; left: 0; right: 0; top: 345px; text-align: center; color: var(--ink);
    font-family: "Ultra", Georgia, serif;
  }
  .logo .small { display: block; font-size: 8px; letter-spacing: 1.5px; }
  .logo .name { display: block; font-size: 22px; letter-spacing: 2px; line-height: 1.1; }
  .tagline {
    position: absolute; left: 0; right: 0; top: 437px; text-align: center; color: var(--red);
    font-family: "Oswald", Arial, sans-serif; font-weight: 500; font-size: 12px; letter-spacing: 1.6px;
  }
  .url-band {
    position: absolute; left: 0; right: 0; bottom: 0; height: 38px; background: var(--red);
    color: var(--white); text-align: center; line-height: 38px;
    font-family: "Oswald", Arial, sans-serif; font-weight: 500; font-size: 14px; letter-spacing: 3.5px;
  }
</style>
</head>
<body>

<svg width="0" height="0" style="position:absolute">
  <defs>
    <g id="reopen-ribbon">
      <polygon points="0,0 125,0 125,125" fill="#ad2427"/>
      <g transform="translate(78,47) rotate(45)" fill="#ffffff" font-family="Ultra, Georgia, serif" text-anchor="middle">
        <text x="0" y="-8" font-size="10" letter-spacing="1.5">REOPENS</text>
        <text x="0" y="12" font-size="20">MAY 1</text>
      </g>
      <polygon points="107,8 110,16 118,16 112,21 114,29 107,24 100,29 102,21 96,16 104,16" fill="#ffffff"/>
    </g>
    <polygon id="torn-edge" points="0,8 40,6 90,9 150,5 210,8 260,6 320,9 380,5 440,8 505,6 505,14 0,14" fill="#f6f3e8"/>
  </defs>
</svg>

<article class="ad ad--chip">
  <div class="photo photo--chip" role="img" aria-label="Close-up photo of chocolate chip cookies on a plate"></div>
  <svg class="torn" viewBox="0 0 505 14" preserveAspectRatio="none"><use href="#torn-edge"/></svg>
  <div class="headline">
    <span style="top:74px;font-size:40px;letter-spacing:5px">THE <em>WAIT</em></span>
    <span style="top:126px;font-size:62px;letter-spacing:4px">IS</span>
    <span style="top:188px;font-size:70px;letter-spacing:6px">OVER</span>
  </div>
  <svg class="ribbon" viewBox="0 0 125 125"><use href="#reopen-ribbon"/></svg>
  <div class="logo"><span class="small">A HARBOR</span><span class="name">CRUMB</span><span class="small">BAKERY</span></div>
  <div class="tagline">GLUTEN FREE NEVER LOOKED SO GOOD</div>
  <div class="url-band">WWW.CRUMBOVENHOUSE.COM</div>
</article>

<article class="ad ad--gluten">
  <div class="photo photo--gluten" role="img" aria-label="Photo of chocolate cookie sandwiches with cream filling"></div>
  <svg class="torn" viewBox="0 0 505 14" preserveAspectRatio="none"><use href="#torn-edge"/></svg>
  <div class="headline">
    <span style="top:40px;font-size:34px;letter-spacing:5px">HAVE</span>
    <span style="top:88px;font-size:34px;letter-spacing:4px">A <em>GLUTEN</em></span>
    <span style="top:135px;font-size:50px;letter-spacing:4px">FREE <small style="font-size:32px">DAY</small></span>
    <span style="top:196px;font-size:32px;letter-spacing:4px">ON THE</span>
    <span style="top:243px;font-size:32px;letter-spacing:3px">1<sup style="font-size:16px">ST</sup> OF MAY</span>
  </div>
  <svg class="ribbon" viewBox="0 0 125 125"><use href="#reopen-ribbon"/></svg>
  <div class="logo"><span class="small">A HARBOR</span><span class="name">CRUMB</span><span class="small">BAKERY</span></div>
  <div class="tagline">GLUTEN FREE NEVER LOOKED SO GOOD</div>
  <div class="url-band">WWW.CRUMBOVENHOUSE.COM</div>
</article>

<article class="ad ad--oat">
  <div class="photo photo--oat" role="img" aria-label="Photo of stacked oatmeal cookie sandwiches with white cream filling"></div>
  <svg class="torn" viewBox="0 0 505 14" preserveAspectRatio="none"><use href="#torn-edge"/></svg>
  <div class="headline">
    <span style="top:74px;font-size:40px;letter-spacing:5px">THE <em>WAIT</em></span>
    <span style="top:126px;font-size:62px;letter-spacing:4px">IS</span>
    <span style="top:188px;font-size:70px;letter-spacing:6px">OVER</span>
  </div>
  <svg class="ribbon" viewBox="0 0 125 125"><use href="#reopen-ribbon"/></svg>
  <div class="logo"><span class="small">A HARBOR</span><span class="name">CRUMB</span><span class="small">BAKERY</span></div>
  <div class="tagline">GLUTEN FREE NEVER LOOKED SO GOOD</div>
  <div class="url-band">WWW.CRUMBOVENHOUSE.COM</div>
</article>

</body>
</html>
```